Food Festival "Signature Cocktail" Booth Banner

Need a 3'x9'6" (36" tall x 114" wide) Outdoor Banner for a new "Signature Cocktail" booth at an outdoor food festival. Pellston Onion Jubilee is a non profit festival and the World Record largest Garlic Festival with average of 100K attendees over 3 days. Actual drink served will vary from year to year, but banner for the booth with be reused each year so it will be non drink specific. Banner needs to catch attendee's attention both at a quick glance and from a distance outdoors to drive traffic and sales to the booth. It will be mounted above the sales window of a 10x10 Festival Booth on PVC frame (see attached pic for reference). "Signature Cocktail" is required text along with it being identified as a Pellston Onion Jubilee booth either through use of attached logo (color can be modified) or "Pellston Onion Jubilee" text since we also have for profit competing vendors. Banner will be full color print. Idea concepts: Neon Sign, Art Deco elegant, reclaimed wood...but open to any concepts. Festival website: https://pellstononionjubilee.example

Target Market(s)

Food Festival Attendees

Font styles to use
Decorative
Script
Other font styles liked:
• Neon, heavy weight fonts, open.

Colors

Designer to choose colors to be used in the design.

Requirements
Must have
• "Signature Cocktail" and "Pellston Onion Jubilee" text or POJ Logo provided, colors and layout that stands out and easily identifiable and readable from a long distance with strong text
Nice to have
• Vibrant engaging background,, ties to Garlic
Should not have
• Clip art, generic text

```html
<!DOCTYPE html>
<html lang="en">
<head>
<meta charset="utf-8">
<title>Pellston Onion Jubilee – Signature Cocktail Booth Banner</title>
<link rel="stylesheet" href="https://fonts.googleapis.com/css2?family=Fredoka:wght@700&display=swap">
<style>
  :root {
    --backdrop: #2a2a2a;
    --green-light: #a6d41c;
    --green-mid: #5fb51f;
    --green-deep: #2f8f16;
    --white: #ffffff;
    --coral: #ee5a3c;
    --purple-top: #c457b8;
    --purple-bottom: #a3168f;
  }
  html, body {
    margin: 0;
    padding: 0;
    width: 1200px;
    height: 960px;
    overflow: hidden;
    background: var(--backdrop);
  }
  .canvas {
    position: relative;
    width: 1200px;
    height: 960px;
  }
  .banner {
    position: absolute;
    left: 20px;
    top: 297px;
    width: 1160px;
    height: 366px;
    display: block;
    font-family: "Fredoka", "Arial Rounded MT Bold", sans-serif;
  }
  .festival-name {
    font-weight: 700;
    fill: var(--white);
  }
  .headline {
    font-weight: 700;
    paint-order: stroke fill;
    stroke-linejoin: round;
  }
  .headline--signature {
    fill: var(--white);
    stroke: var(--coral);
    stroke-width: 6px;
  }
  .headline--cocktail {
    fill: url(#cocktail-fill);
    stroke: var(--white);
    stroke-width: 7px;
  }
</style>
</head>
<body>
<main class="canvas">
  <svg class="banner" viewBox="0 0 1160 366" xmlns="http://www.w3.org/2000/svg" aria-labelledby="banner-title">
    <title id="banner-title">Pellston Onion Jubilee Signature Cocktail banner</title>
    <defs>
      <radialGradient id="field-glow" cx="0.62" cy="0.1" r="0.9">
        <stop offset="0" stop-color="var(--green-light)"/>
        <stop offset="0.55" stop-color="var(--green-mid)"/>
        <stop offset="1" stop-color="var(--green-deep)"/>
      </radialGradient>
      <linearGradient id="cocktail-fill" x1="0" y1="0" x2="0" y2="1">
        <stop offset="0" stop-color="var(--purple-top)"/>
        <stop offset="0.5" stop-color="var(--purple-top)"/>
        <stop offset="0.5" stop-color="var(--purple-bottom)"/>
        <stop offset="1" stop-color="var(--purple-bottom)"/>
      </linearGradient>
    </defs>

    <rect class="banner-field" width="1160" height="366" fill="url(#field-glow)"
          role="img" aria-label="Green background with a faint line-drawn garlic bulb pattern"/>

    <g class="festival-mark" aria-label="Pellston Onion Jubilee">
      <text class="festival-name" x="178" y="150" font-size="40" text-anchor="middle">Pellston</text>
      <text class="festival-name" x="178" y="198" font-size="40" text-anchor="middle">Onion</text>
      <text class="festival-name" x="178" y="246" font-size="40" text-anchor="middle">Jubilee</text>
    </g>

    <text class="headline headline--signature" x="348" y="154" font-size="116"
          textLength="597" lengthAdjust="spacingAndGlyphs">SIGNATURE</text>
    <text class="headline headline--cocktail" x="348" y="300" font-size="168"
          textLength="758" lengthAdjust="spacingAndGlyphs">COCKTAIL</text>
  </svg>
</main>
</body>
</html>
```